FIELDLINE CIVIC ATHLETIDOME INVESTMENT BROCHURE*

We need an investment brochure for a new sportsplex being built to service the Greater Toronto Area. The attached file called "Brochure 2020" can be repurposed, with the Fieldline Civic Athletidome name and logo inserted wherever the Fieldline Civic Athletidome info currently exists.

We have also provided an excel file with 3 sheets-- each of these sheets is to be inserted into the brochure.

Target Market(s)

Investors

Logo Text

FIELDLINE ATHLETIDOME

Requirements
Must have
• Project must reference:
The Worldwide trend to small sided soccer.

Investment opportunity that is eligible for registered funds (RRSPs and TFSAs)

Fieldline Civic Athletidome is a unique combination of sport and court that allows both players and spectators to be immersed with a fast-paced, high-energy game.
Should not have
• No wording or pages that reference "American" or USA.

```html
<!DOCTYPE html>
<html lang="en">
<head>
<meta charset="utf-8">
<title>Getting Started – Project Design Fee</title>
<link rel="stylesheet" href="https://fonts.googleapis.com/css2?family=Bebas+Neue&family=Open+Sans:ital,wght@0,400;0,700;1,400&display=swap">
<style>
  :root {
    --navy-deep: #1e1d2e;
    --slate: #4a5e82;
    --ink: #1f2a44;
    --gold: #dcc35e;
    --white: #ffffff;
    --mist: #e7e8eb;
    --black: #111111;
  }
  * { box-sizing: border-box; margin: 0; padding: 0; }
  html, body { width: 1200px; height: 675px; overflow: hidden; background: var(--navy-deep); }
  .slide { position: relative; width: 1200px; height: 675px; background: var(--navy-deep); overflow: hidden; }

  .title-frame {
    position: absolute; left: -4px; top: 38px; width: 604px; height: 170px;
    border: 3px solid var(--white);
  }
  .title-frame h1 {
    position: absolute; left: 36px; top: 42px;
    font-family: "Bebas Neue", sans-serif; font-weight: 400;
    font-size: 63px; line-height: 1; color: var(--white);
    transform: scaleX(0.88); transform-origin: left top; white-space: nowrap;
  }
  .title-frame .tagline {
    position: absolute; left: 35px; top: 104px;
    font-family: Arial, Helvetica, sans-serif; font-style: italic;
    font-size: 20px; color: var(--gold);
  }

  .stage-label {
    position: absolute; left: 4px; width: 102px; text-align: center;
    font-family: Arial, Helvetica, sans-serif; font-style: italic;
    font-size: 15px; line-height: 14.5px; color: var(--gold);
  }
  .stage-label.rendering { top: 263px; }
  .stage-label.final { top: 563px; }
  .stage-arrow { position: absolute; left: 42px; top: 340px; }

  .photo { position: absolute; left: 115px; width: 485px; height: 189px; }
  .photo.rendering { top: 243px; background: linear-gradient(160deg, #5f8f3e 0%, #2f7a2a 45%, #3d8c2e 70%, #7b7f78 100%); }
  .photo.final { top: 446px; background: linear-gradient(180deg, #3f5a32 0%, #8c8a86 30%, #6fb63a 60%, #86c83f 100%); }

  .fee-panel { position: absolute; left: 650px; top: 38px; width: 512px; height: 599px; background: var(--white); overflow: hidden; }
  .fee-panel .backdrop { position: absolute; left: 0; top: 0; }

  .fee-title {
    position: absolute; left: 53px; top: 60px;
    font-family: "Bebas Neue", sans-serif; white-space: nowrap; line-height: 1;
    transform: scaleX(0.86); transform-origin: left top;
  }
  .fee-title .lead { font-size: 48px; color: var(--slate); }
  .fee-title .main { font-size: 64px; color: var(--ink); }

  .brand-name {
    position: absolute; left: 378px; top: 67px; width: 114px; text-align: center;
    font-family: "Bebas Neue", sans-serif; line-height: 1; color: var(--black);
  }
  .brand-name .top { display: block; font-size: 29px; }
  .brand-name .bottom { display: block; font-size: 21px; }

  .partner-dot { position: absolute; left: 421px; top: 152px; width: 22px; height: 22px; border-radius: 50%; background: var(--ink); }
  .partner-name {
    position: absolute; left: 388px; top: 182px; width: 88px; text-align: center;
    font-family: "Bebas Neue", sans-serif; font-size: 17px; line-height: 17px; color: var(--ink);
  }

  .package-outline { position: absolute; left: 48px; top: 135px; width: 329px; height: 81px; border: 1.5px solid var(--gold); }
  .package-card { position: absolute; left: 54px; top: 142px; width: 315px; height: 104px; background: var(--slate); }
  .package-card .field-icon { position: absolute; left: 38px; top: 26px; }
  .package-card h2 {
    position: absolute; left: 154px; top: 29px;
    font-family: "Bebas Neue", sans-serif; font-weight: 400; font-size: 24px; line-height: 1; color: var(--white);
    transform: scaleX(0.86); transform-origin: left top; white-space: nowrap;
  }
  .package-card .price {
    position: absolute; left: 165px; top: 54px;
    font-family: "Bebas Neue", sans-serif; font-size: 24px; line-height: 1; color: var(--gold);
    transform: scaleX(0.86); transform-origin: left top;
  }
  .package-card .price-note {
    position: absolute; left: 210px; top: 57px; width: 64px; text-align: center;
    font-family: "Open Sans", sans-serif; font-size: 7.5px; line-height: 8.5px; color: var(--white);
  }
  .package-rule { position: absolute; left: 55px; top: 252px; width: 321px; height: 1px; background: var(--gold); }

  .inclusions { position: absolute; left: 47px; top: 267px; width: 418px; height: 300px; background: var(--slate); list-style: none; }
  .inclusions li {
    position: absolute; left: 108px; width: 204px; height: 33px;
    box-shadow: inset 0 -1px 0 var(--gold);
    display: flex; align-items: center; justify-content: center;
    font-family: "Open Sans", sans-serif; font-weight: 700; font-size: 9.8px; color: var(--white); white-space: nowrap;
  }
  .inclusions .fine-print {
    position: absolute; left: 0; top: 279px; width: 418px; text-align: center;
    font-family: "Open Sans", sans-serif; font-style: italic; font-size: 7.5px; color: var(--white);
  }
</style>
</head>
<body>
<main class="slide">
  <header class="title-frame">
    <h1>Getting Started</h1>
    <p class="tagline">Equipping You For Success</p>
  </header>

  <p class="stage-label rendering">PROJECT<br>SPECIFIC<br>RENDERING</p>
  <svg class="stage-arrow" width="26" height="186" viewBox="0 0 26 186" aria-hidden="true">
    <line x1="13" y1="0" x2="13" y2="168" stroke="#ffffff" stroke-width="3"/>
    <polygon points="1,166 25,166 13,184" fill="#ffffff"/>
  </svg>
  <p class="stage-label final">FINAL<br>PRODUCT<br>PHOTO</p>

  <div class="photo rendering" role="img" aria-label="Rendering of a fenced small-sided turf field beside a building with players in a match"></div>
  <div class="photo final" role="img" aria-label="Photo of a completed backyard turf court with white boards, goal and net"></div>

  <section class="fee-panel">
    <svg class="backdrop" width="512" height="599" viewBox="0 0 512 599" aria-hidden="true">
      <path d="M0 190 Q 200 150 512 160 L512 599 L0 599 Z" fill="#e7e8eb"/>
      <path d="M0 300 Q 260 230 512 250 L512 599 L0 599 Z" fill="#dfe0e4" opacity="0.6"/>
    </svg>

    <div class="fee-title"><span class="lead">Project</span> <span class="main">Design Fee</span></div>
    <p class="brand-name"><span class="top">FIELDLINE</span><span class="bottom">ATHLETIDOME</span></p>
    <div class="partner-dot"></div>
    <p class="partner-name">FIELDLINE<br>CIVIC<br>ATHLETIDOME</p>

    <div class="package-outline"></div>
    <div class="package-card">
      <svg class="field-icon" width="90" height="52" viewBox="0 0 90 52" aria-hidden="true" fill="none" stroke="#ffffff" stroke-width="1.3">
        <rect x="1" y="1" width="88" height="50"/>
        <line x1="45" y1="1" x2="45" y2="51"/>
        <circle cx="45" cy="26" r="8"/>
        <rect x="1" y="14" width="13" height="24"/>
        <rect x="76" y="14" width="13" height="24"/>
      </svg>
      <h2>Project Package:</h2>
      <span class="price">$2,500</span>
      <span class="price-note">applied towards end balance</span>
    </div>
    <div class="package-rule"></div>

    <ul class="inclusions">
      <li style="top:4px">Personal Project Consultant</li>
      <li style="top:37px">Project Specific Renderings &amp; Site Plan</li>
      <li style="top:71px">Financing Packet</li>
      <li style="top:104px">Site Requirements</li>
      <li style="top:138px">Field Drawings</li>
      <li style="top:171px">Lighting and Electrical Engineering Information</li>
      <li style="top:205px">Pro Forma Financial Statement for 1 or 2 Fields</li>
      <li style="top:238px">(1) Site Visit From Your Project Consultant</li>
      <p class="fine-print">nonrefundable, applied towards end project balance</p>
    </ul>
  </section>
</main>
</body>
</html>
```